Business cards / Stationery
Stationery
Professional
Tomas Belcourt
DOE, CPT, LMT
1400 North Pelham Road
Harlow Springs, Texas 78412
tomas.belcourt@merrowcareclinic.com
www.merrowcareclinic.com

```html
<!DOCTYPE html>
<html lang="en">
<head>
<meta charset="utf-8">
<title>Merrow Care Stationery</title>
<link href="https://fonts.googleapis.com/css2?family=Open+Sans:wght@400;600;700;800&display=swap" rel="stylesheet">
<style>
:root{
  --bg:#e9e6e1;
  --paper:#ffffff;
  --blue:#1f9ad6;
  --grey-band:#8f9194;
  --ink:#3a3d40;
  --muted:#8a8d90;
  --faint:#eef3f7;
  --dark-card-1:#6a6c6f;
  --dark-card-2:#3c3e41;
}
*{box-sizing:border-box;margin:0;padding:0}
html,body{width:1200px;height:514px;overflow:hidden;background:var(--bg);font-family:"Open Sans",Arial,sans-serif;color:var(--ink)}
.sheet{position:absolute;background:var(--paper);box-shadow:0 2px 6px rgba(0,0,0,.18);overflow:hidden}
.brand{position:absolute;display:flex;align-items:center;gap:5px}
.brand-dot{width:14px;height:14px;border-radius:50%;background:var(--blue);flex:none}
.brand-name{font-weight:800;color:var(--blue);font-size:11px;letter-spacing:.3px;white-space:nowrap}
.rule{position:absolute;height:3px;background:var(--blue)}
.rule-tab{position:absolute;height:7px;background:var(--grey-band)}
.watermark{position:absolute;border-radius:50%;background:var(--faint)}
.footer{position:absolute;display:flex;gap:18px;font-size:4.5px;color:var(--muted);line-height:1.5;white-space:nowrap}
.footer span{display:block}
.footer .ico{display:inline-block;width:4px;height:4px;border-radius:50%;background:var(--blue);margin-right:3px;vertical-align:middle}
.letterhead{left:43px;top:40px;width:341px;height:430px}
.fax{left:408px;top:40px;width:336px;height:430px}
.fax-title{position:absolute;left:18px;top:92px;font-size:20px;font-weight:400;color:var(--ink)}
.fax-fields{position:absolute;left:18px;top:128px;width:300px;display:grid;grid-template-columns:1fr 1fr;column-gap:24px;row-gap:9px;font-size:5px}
.field{display:flex;align-items:flex-end;gap:4px}
.field i{flex:1;border-bottom:.6px solid #b8babc;height:6px}
.fax-checks{position:absolute;left:18px;top:210px;display:flex;gap:16px;font-size:4.8px}
.fax-checks span{display:flex;align-items:center;gap:3px}
.fax-checks b{width:6px;height:6px;border:.7px solid #777}
.fax-divider{position:absolute;left:18px;right:18px;top:200px;height:.6px;background:#c9cbcd}
.card-front{left:773px;top:36px;width:211px;height:120px;border-radius:6px}
.card-front .who{position:absolute;left:12px;top:70px;font-size:5px;line-height:1.55;color:var(--ink);white-space:nowrap}
.card-front .who strong{font-size:6.5px;color:var(--blue)}
.card-appt{left:991px;top:36px;width:190px;height:120px;border-radius:6px}
.appt-title{position:absolute;left:12px;top:10px;font-size:6.5px;font-weight:700;color:var(--blue)}
.appt-rows{position:absolute;left:12px;top:24px;width:166px;font-size:4.8px;display:flex;flex-direction:column;gap:9px}
.card-back{left:888px;top:165px;width:182px;height:96px;border-radius:7px;background:linear-gradient(180deg,var(--dark-card-1),var(--dark-card-2))}
.card-back .site{position:absolute;left:0;right:0;top:60px;text-align:center;color:#fff;font-size:5px;letter-spacing:.2px}
.envelope{left:809px;top:340px;width:372px;height:140px}
</style>
</head>
<body>

<section class="sheet letterhead">
  <div class="brand" style="left:16px;top:16px"><span class="brand-dot"></span><span class="brand-name">MERROW CARE</span></div>
  <div class="rule-tab" style="left:0;top:52px;width:16px"></div>
  <div class="rule" style="left:16px;right:0;top:54px"></div>
  <div class="watermark" style="left:110px;top:160px;width:120px;height:120px"></div>
  <div class="rule" style="left:0;right:0;bottom:22px;height:1px;background:#d5d7d9"></div>
  <div class="footer" style="left:16px;bottom:6px">
    <div><span><i class="ico"></i>1400 North Pelham Road</span><span>Harlow Springs, Texas 78412</span></div>
    <div><span><i class="ico"></i>(512) 555-0142</span><span>(512) 555-0143</span></div>
    <div><span><i class="ico"></i>tomas.belcourt@merrowcareclinic.com</span><span>www.merrowcareclinic.com</span></div>
  </div>
</section>

<section class="sheet fax">
  <div class="brand" style="left:16px;top:16px"><span class="brand-dot"></span><span class="brand-name">MERROW CARE</span></div>
  <div class="rule-tab" style="left:0;top:52px;width:16px"></div>
  <div class="rule" style="left:16px;right:0;top:54px"></div>
  <h1 class="fax-title">FAX</h1>
  <div class="fax-fields">
    <div class="field">To:<i></i></div><div class="field">Fax:<i></i></div>
    <div class="field">From:<i></i></div><div class="field">Pages:<i></i></div>
    <div class="field">Phone:<i></i></div><div class="field">Date:<i></i></div>
    <div class="field">Re:<i></i></div><div class="field">CC:<i></i></div>
  </div>
  <div class="fax-divider"></div>
  <div class="fax-checks">
    <span><b></b>Urgent</span><span><b></b>For Review</span><span><b></b>Please Comment</span><span><b></b>Please Reply</span><span><b></b>Please Recycle</span>
  </div>
  <div class="rule" style="left:0;right:0;bottom:22px;height:1px;background:#d5d7d9"></div>
  <div class="footer" style="left:16px;bottom:6px">
    <div><span><i class="ico"></i>1400 North Pelham Road</span><span>Harlow Springs, Texas 78412</span></div>
    <div><span><i class="ico"></i>(512) 555-0142</span><span>(512) 555-0143</span></div>
    <div><span><i class="ico"></i>tomas.belcourt@merrowcareclinic.com</span><span>www.merrowcareclinic.com</span></div>
  </div>
</section>

<section class="sheet card-front">
  <div class="watermark" style="left:120px;top:20px;width:80px;height:80px"></div>
  <div class="brand" style="left:12px;top:14px"><span class="brand-dot"></span><span class="brand-name">MERROW CARE</span></div>
  <div class="rule-tab" style="left:0;top:50px;width:12px;height:5px"></div>
  <div class="rule" style="left:12px;right:0;top:51px;height:2px"></div>
  <div class="who">
    <strong>Tomas Belcourt</strong> DOE, CPT, LMT<br>
    1400 North Pelham Road, Harlow Springs, Texas 78412<br>
    tomas.belcourt@merrowcareclinic.com
  </div>
</section>

<section class="sheet card-appt">
  <div class="watermark" style="left:95px;top:25px;width:80px;height:80px"></div>
  <div class="appt-title">Next Appointment</div>
  <div class="appt-rows">
    <div class="field">Name<i></i></div>
    <div class="field">Date<i></i>Time<i></i></div>
    <div class="field">Date<i></i>Time<i></i></div>
    <div class="field">Date<i></i>Time<i></i></div>
  </div>
</section>

<section class="sheet card-back">
  <div style="position:absolute;left:83px;top:24px;width:16px;height:16px;border-radius:50%;background:#7a7c7f"></div>
  <div class="site">www.merrowcareclinic.com</div>
</section>

<section class="sheet envelope">
  <div class="brand" style="left:14px;top:14px"><span class="brand-dot"></span><span class="brand-name">MERROW CARE</span></div>
  <div class="watermark" style="left:255px;top:22px;width:90px;height:90px"></div>
  <div class="rule-tab" style="left:0;top:104px;width:14px;height:5px"></div>
  <div class="rule" style="left:14px;right:0;top:105px;height:2px"></div>
  <div class="footer" style="left:14px;bottom:6px">
    <div><span><i class="ico"></i>1400 North Pelham Road, Harlow Springs, Texas 78412</span></div>
    <div><span><i class="ico"></i>www.merrowcareclinic.com</span></div>
  </div>
</section>

</body>
</html>
```